TopMoneyswitch.net Mobile App

Topmoneyswitch.net is an online Beurea de change. They buy and sell currency from individuals and large corporations.

The app will compliment the main website of the company and focus on specific features as set out in our brief document. overall the design must be high-quality, easy navigate with a one finger operation and nice clean design.

This content is for the design of 3 screen

Loading screen
Homepage screen
Buy Currency for Branch Collection screen

attached is a full brief, but the loading screen will incorporate the logo and the home screen must allow easy navigation to 6 key button features that will enable you to go to each section of the app.

The winner will get to design the remaining screens of the app which are approx 15/18 further screens, based on the same layout.

If you can code the app as well into iPhone and Android, please make this known as well.
Updates

Hello,

For further inspritation for the Home screen, we quite like the interface on the uploaded image vellorin-home.jpg

So you slide left and right with your finger to the button, instead of a list format or something quite 2d. Almost 3d like interface maybe with an option to display all as a list?

See what sort of creativity can be achieved.

thanks

Target Market(s)

Consumers mainly aged between 25-60

Industry/Entity Type

It Company

Requirements
Must have
• good clean visually stunning appearance with apply shiny effect buttons and navigation

```html
<!DOCTYPE html>
<html lang="en">
<head>
<meta charset="utf-8">
<title>TopMoneyswitch.net Mobile App Screens</title>
<link rel="stylesheet" href="https://fonts.googleapis.com/css2?family=Open+Sans:wght@400;600;700&family=Exo+2:wght@500;600&display=swap">
<style>
  :root {
    --page: #ffffff;
    --brand-red: #e0303c;
    --brand-blue: #1f5a96;
    --label-blue: #5b8fc6;
    --pink: #e0356b;
    --ink: #333333;
    --muted: #8a8a8a;
    --metal-light: #ececec;
    --metal-dark: #cfcfcf;
    --panel-line: #a9a9a9;
    --icon: #3c3c3c;
    --bar-blue: #2d6fb0;
  }
  * { box-sizing: border-box; margin: 0; padding: 0; }
  html, body { width: 1200px; height: 666px; overflow: hidden; background: var(--page); }
  body { position: relative; font-family: "Open Sans", Arial, sans-serif; color: var(--ink); }

  .screen {
    position: absolute; top: 155px; width: 220px; height: 328px; overflow: hidden;
    border: 1px solid #b9b9b9;
  }
  .screen--loading { left: 40px; background: linear-gradient(160deg, #ffffff 0%, #f4f4f4 55%, #e9e9e9 100%); }
  .screen--login { left: 334px; background: linear-gradient(180deg, #e4e4e4, #d6d6d6); }
  .screen--home { left: 630px; background: linear-gradient(180deg, var(--metal-light), var(--metal-dark)); }
  .screen--feature { left: 926px; background: linear-gradient(180deg, var(--metal-light), var(--metal-dark)); }

  .brand { position: absolute; left: 0; width: 220px; text-align: center; }
  .brand__name { font-size: 19px; font-weight: 700; color: var(--brand-blue); letter-spacing: -0.3px; line-height: 1.1; }
  .brand__tagline { font-size: 9px; font-weight: 600; color: var(--ink); letter-spacing: 0.6px; margin-top: 4px; }

  .loading-bar {
    position: absolute; left: 6px; right: 6px; bottom: 6px; height: 12px; border-radius: 3px;
    border: 1px solid #bcbcbc;
    background: repeating-linear-gradient(-55deg, var(--bar-blue) 0 7px, #ffffff 7px 14px);
  }

  .login-panel {
    position: absolute; left: 7px; top: 171px; width: 206px; height: 64px; border-radius: 3px;
    background: rgba(255,255,255,0.25); border: 1px solid #c4c4c4;
  }
  .login-row { position: absolute; left: 12px; display: flex; align-items: center; }
  .login-row label { width: 92px; font-size: 14px; font-weight: 700; color: var(--label-blue); }
  .login-row span { display: block; width: 98px; height: 20px; background: #fff; border: 1px solid #b5b5b5; }
  .btn {
    position: absolute; left: 24px; width: 178px; height: 28px; border: 1px solid #b0b0b0; border-radius: 2px;
    background: linear-gradient(180deg, #ffffff, #e6e6e6); font-size: 13px; font-weight: 600;
    display: flex; align-items: center; justify-content: center;
  }
  .btn--primary { top: 242px; color: var(--pink); }
  .btn--secondary { top: 281px; color: var(--muted); }

  .menu-panel {
    position: absolute; left: 7px; top: 100px; width: 208px; height: 185px; border-radius: 8px;
    border: 1px solid var(--panel-line); background: rgba(255,255,255,0.25);
    box-shadow: inset 0 0 0 3px rgba(255,255,255,0.5);
  }
  .menu-item { position: absolute; width: 64px; text-align: center; }
  .menu-item__button {
    width: 54px; height: 54px; margin: 0 auto; border-radius: 50%;
    background: radial-gradient(circle at 50% 30%, #ffffff 0%, #e4e4e4 55%, #bdbdbd 100%);
    border: 1px solid #a8a8a8; box-shadow: 0 1px 2px rgba(0,0,0,0.25);
    display: flex; align-items: center; justify-content: center;
  }
  .menu-item__label { font-size: 7px; line-height: 9px; color: #444; margin-top: 3px; }

  .tab-bar { position: absolute; left: 0; top: 292px; width: 220px; height: 36px; }
  .tab {
    position: absolute; border-radius: 50%; display: flex; align-items: center; justify-content: center;
    background: radial-gradient(circle at 50% 30%, #ffffff, #d8d8d8 70%, #b9b9b9);
    border: 1px solid #9f9f9f;
  }
  .tab--fav { left: 15px; top: 4px; width: 24px; height: 24px; }
  .tab--home { left: 94px; top: -2px; width: 34px; height: 34px; }
  .tab--info { left: 180px; top: 4px; width: 24px; height: 24px; }

  .feature-head { position: absolute; left: 12px; top: 15px; display: flex; align-items: center; }
  .feature-head__icon {
    width: 52px; height: 52px; border-radius: 50%; border: 2px solid #d0d0d0;
    background: radial-gradient(circle at 50% 30%, #7fb2e6, #2b6db2 60%, #1b4f88);
    display: flex; align-items: center; justify-content: center;
  }
  .feature-head__title {
    width: 128px; height: 24px; margin-left: -4px; padding-left: 12px;
    background: linear-gradient(180deg, #fafafa, #e3e3e3); border: 1px solid #c4c4c4;
    font-family: "Exo 2", "Open Sans", sans-serif; font-size: 14px; font-weight: 500; color: #333;
    display: flex; align-items: center;
  }
  .feature-copy { position: absolute; left: 14px; width: 180px; font-size: 6.6px; line-height: 8.6px; color: #333; }
  .pager {
    position: absolute; left: 121px; top: 152px; width: 80px; height: 18px; border-radius: 9px;
    background: linear-gradient(180deg, #fafafa, #dedede); border: 1px solid #c2c2c2;
  }
  .pager__btn {
    position: absolute; top: 0; width: 18px; height: 16px; border-radius: 50%;
    display: flex; align-items: center; justify-content: center;
  }
</style>
</head>
<body>

<!-- Loading screen -->
<section class="screen screen--loading" aria-label="Loading screen">
  <div class="brand" style="top:128px">
    <div class="brand__name">TopMoneyswitch.net</div>
    <div class="brand__tagline">CURRENCY SPECIALISTS</div>
  </div>
  <div class="loading-bar" role="progressbar" aria-label="Loading"></div>
</section>

<!-- Sign in screen -->
<section class="screen screen--login" aria-label="Sign in screen">
  <div class="brand" style="top:80px">
    <div class="brand__name">TopMoneyswitch.net</div>
    <div class="brand__tagline">CURRENCY SPECIALISTS</div>
  </div>
  <div class="login-panel">
    <div class="login-row" style="top:8px"><label>Username</label><span></span></div>
    <div class="login-row" style="top:34px"><label>Password</label><span></span></div>
  </div>
  <div class="btn btn--primary">Sign In</div>
  <div class="btn btn--secondary">Create New Account</div>
</section>

<!-- Home screen -->
<section class="screen screen--home" aria-label="Home screen">
  <div class="brand" style="top:32px">
    <div class="brand__name">TopMoneyswitch.net</div>
    <div class="brand__tagline">CURRENCY SPECIALISTS</div>
  </div>
  <div class="menu-panel">
    <div class="menu-item" style="left:9px;top:16px">
      <div class="menu-item__button"><svg width="26" height="20" viewBox="0 0 26 20"><path d="M2 2l9 8-9 8M13 2l9 8-9 8" fill="none" stroke="var(--icon)" stroke-width="3.5" stroke-linejoin="round"/></svg></div>
      <div class="menu-item__label">Fast<br>Track</div>
    </div>
    <div class="menu-item" style="left:72px;top:16px">
      <div class="menu-item__button"><span style="font-size:30px;font-weight:700;color:var(--icon)">$</span></div>
      <div class="menu-item__label">Buy<br>Currency</div>
    </div>
    <div class="menu-item" style="left:135px;top:16px">
      <div class="menu-item__button"><svg width="26" height="26" viewBox="0 0 26 26"><circle cx="10" cy="10" r="7" fill="none" stroke="var(--icon)" stroke-width="3.5"/><path d="M15 15l8 8" stroke="var(--icon)" stroke-width="4.5" stroke-linecap="round"/></svg></div>
      <div class="menu-item__label">Locate<br>Stores</div>
    </div>
    <div class="menu-item" style="left:9px;top:101px">
      <div class="menu-item__button"><svg width="40" height="34" viewBox="0 0 40 34"><text x="2" y="17" font-family="Open Sans, sans-serif" font-size="18" font-weight="700" fill="var(--icon)">$</text><text x="24" y="32" font-family="Open Sans, sans-serif" font-size="17" font-weight="700" fill="var(--icon)">£</text><path d="M15 11h10l-3-3M25 22H15l3 3" fill="none" stroke="var(--icon)" stroke-width="2.2"/></svg></div>
      <div class="menu-item__label">Converter</div>
    </div>
    <div class="menu-item" style="left:72px;top:101px">
      <div class="menu-item__button"><svg width="26" height="28" viewBox="0 0 26 28"><path d="M8 24V5M3 10l5-6 5 6M18 4v19M13 18l5 6 5-6" fill="none" stroke="var(--icon)" stroke-width="3"/></svg></div>
      <div class="menu-item__label">Live Rates</div>
    </div>
    <div class="menu-item" style="left:135px;top:101px">
      <div class="menu-item__button"><svg width="28" height="28" viewBox="0 0 28 28"><circle cx="14" cy="14" r="9" fill="none" stroke="var(--icon)" stroke-width="5" stroke-dasharray="4.2 2.9"/><circle cx="14" cy="14" r="7" fill="var(--icon)"/><circle cx="14" cy="14" r="3" fill="#e4e4e4"/></svg></div>
      <div class="menu-item__label">Preferences</div>
    </div>
  </div>
  <nav class="tab-bar">
    <div class="tab tab--fav"><svg width="14" height="14" viewBox="0 0 24 24"><path d="M12 2l3 7 7 .6-5.3 4.7 1.6 7.2L12 17.8 5.7 21.5l1.6-7.2L2 9.6 9 9z" fill="var(--icon)"/></svg></div>
    <div class="tab tab--home"><svg width="18" height="18" viewBox="0 0 24 24"><path d="M12 3L2 12h3v9h5v-6h4v6h5v-9h3z" fill="var(--icon)"/></svg></div>
    <div class="tab tab--info"><span style="font:italic 700 14px Georgia, serif;color:var(--icon)">i</span></div>
  </nav>
</section>

<!-- Locate Stores screen -->
<section class="screen screen--feature" aria-label="Locate stores screen">
  <div class="brand" style="top:32px">
    <div class="brand__name">TopMoneyswitch.net</div>
    <div class="brand__tagline">CURRENCY SPECIALISTS</div>
  </div>
  <div class="menu-panel" style="top:104px;height:181px">
    <div class="feature-head">
      <div class="feature-head__icon"><svg width="24" height="24" viewBox="0 0 26 26"><circle cx="10" cy="10" r="7" fill="none" stroke="#1a1a1a" stroke-width="3.5"/><path d="M15 15l8 8" stroke="#1a1a1a" stroke-width="4.5" stroke-linecap="round"/></svg></div>
      <div class="feature-head__title">Locate Stores</div>
    </div>
    <p class="feature-copy" style="top:76px">This function allows you to locate the stores close to you. And some more text to describe the function further can be added here.</p>
    <p class="feature-copy" style="top:110px">This function allows you to locate the stores close to you. And some more text to describe the function further can be added here.</p>
    <div class="pager">
      <div class="pager__btn" style="left:0"><svg width="10" height="10" viewBox="0 0 10 10"><path d="M9 5H2M5 1L1 5l4 4" fill="none" stroke="var(--icon)" stroke-width="1.8"/></svg></div>
      <div class="pager__btn" style="right:0"><svg width="10" height="10" viewBox="0 0 10 10"><path d="M1 5h7M5 1l4 4-4 4" fill="none" stroke="var(--icon)" stroke-width="1.8"/></svg></div>
    </div>
  </div>
  <nav class="tab-bar">
    <div class="tab tab--fav"><svg width="14" height="14" viewBox="0 0 24 24"><path d="M12 2l3 7 7 .6-5.3 4.7 1.6 7.2L12 17.8 5.7 21.5l1.6-7.2L2 9.6 9 9z" fill="var(--icon)"/></svg></div>
    <div class="tab tab--home"><svg width="18" height="18" viewBox="0 0 24 24"><path d="M12 3L2 12h3v9h5v-6h4v6h5v-9h3z" fill="var(--icon)"/></svg></div>
    <div class="tab tab--info"><span style="font:italic 700 14px Georgia, serif;color:var(--icon)">i</span></div>
  </nav>
</section>

</body>
</html>
```